Brightwave Partners, Inc. Website redesign

Revamp the website, it is old and outdated. www.brightwavepartnersinc.example

Target Market(s)

Information Technology Consulting and Staffing

Coding

Coded - Design and coding required

Number of Pages Required

5+ page

Colors

Designer to choose colors to be used in the design.

Requirements
Must have
• Outlined text boxes just like from the Tolvane.us site. A clean look

```html
<!DOCTYPE html>
<html lang="en">
<head>
<meta charset="utf-8">
<title>Brightwave Partners, Inc.</title>
<link href="https://fonts.googleapis.com/css2?family=Rubik:wght@500;600&family=Open+Sans:wght@400;600&display=swap" rel="stylesheet">
<style>
:root{
  --red:#8c1730;
  --red-deep:#6e0f22;
  --ink:#1d1d1d;
  --text:#444;
  --muted:#777;
  --band:#e9e9e9;
  --footer:#2b2b2b;
  --footer-bottom:#232323;
  --white:#fff;
}
*{box-sizing:border-box;margin:0;padding:0}
html,body{width:1200px;height:3425px;overflow:hidden;background:var(--white)}
body{position:relative;font-family:"Open Sans",Arial,sans-serif;color:var(--text)}
.abs{position:absolute}
.head{font-family:"Rubik",Arial,sans-serif;font-weight:500;text-transform:uppercase}
/* header */
.call-tab{left:768px;top:0;width:432px;height:41px;background:var(--red);clip-path:polygon(0 0,100% 0,100% 100%,28px 100%);color:#fff;font-family:"Rubik",sans-serif;font-weight:500;font-size:19px;display:flex;align-items:center;padding-left:60px;gap:8px}
.top-line{left:0;top:0;width:1200px;height:4px;background:var(--red)}
.brand{left:133px;top:44px;display:flex;align-items:center;gap:12px;font-family:"Rubik",sans-serif;font-weight:600;font-size:25px;color:var(--ink)}
.brand-mark{width:22px;height:22px;background:var(--red)}
.nav a{position:absolute;top:68px;font-family:"Rubik",sans-serif;font-weight:500;font-size:16px;color:#333;text-decoration:none}
.nav a.active{color:var(--red)}
/* hero */
.hero{left:0;top:117px;width:1200px;height:594px;background:linear-gradient(100deg,#3e4449 0%,#23292d 45%,#15191c 100%)}
.hero-title{left:180px;width:840px;top:340px;text-align:center;color:#fff;font-family:"Rubik",sans-serif;font-weight:500;font-size:41px;white-space:nowrap}
.hero-sub{left:0;width:1200px;top:399px;text-align:center;color:#fff;font-family:"Rubik",sans-serif;font-weight:500;font-size:28px}
.btn-solid{left:501px;top:448px;width:201px;height:56px;background:var(--red);color:#fff;font-family:"Rubik",sans-serif;font-weight:500;font-size:21px;display:flex;align-items:center;justify-content:center}
.circle-arrow{width:52px;height:52px;border-radius:50%;background:rgba(255,255,255,.8);display:flex;align-items:center;justify-content:center}
/* services */
.band{left:0;top:711px;width:1200px;height:388px;background:var(--band)}
.svc{top:654px;width:281px;height:384px;background:#fff;border-top:3px solid var(--red);box-shadow:0 1px 3px rgba(0,0,0,.12)}
.svc h3{position:absolute;left:19px;top:14px;font-family:"Rubik",sans-serif;font-weight:500;font-size:18px;line-height:23px;color:var(--red);text-transform:uppercase}
.svc .pic{position:absolute;left:0;top:70px;width:281px;height:162px}
.svc p{position:absolute;left:24px;top:252px;width:240px;font-size:12px;line-height:17px;color:#333}
.btn-line{border:2px solid var(--red);color:var(--red);font-family:"Rubik",sans-serif;font-weight:500;text-transform:uppercase;display:flex;align-items:center;justify-content:center;background:transparent}
.svc .btn-line{position:absolute;left:24px;top:321px;width:145px;height:41px;font-size:13px}
/* about */
.about-pic{left:173px;top:1203px;width:303px;height:285px;background:linear-gradient(135deg,#1f2c44 0%,#4a5a72 55%,#9aa6b4 100%)}
.about-h{left:532px;top:1212px;width:520px;font-size:27px;line-height:39px;color:var(--ink)}
.about-p{left:532px;top:1302px;width:520px;font-size:18.5px;line-height:26px;color:#555}
/* strategy */
.strategy{left:0;top:1570px;width:1200px;height:497px;background:linear-gradient(90deg,#e3e3e3 0%,#e0e0e0 40%,#d4d8de 100%)}
.strategy-pic{left:439px;top:1570px;width:761px;height:497px;background:linear-gradient(100deg,rgba(228,228,228,0) 0%,#c9cdd3 25%,#d9b9a6 55%,#b8c3cf 80%,#9fb0c2 100%)}
.strat-h{left:162px;top:1690px;font-size:32px;color:var(--red)}
.strat-sub{left:162px;top:1735px;font-size:27px;color:var(--ink)}
.strat-p{left:164px;top:1784px;width:420px;font-size:18px;line-height:27px;color:#444}
/* news */
.news-h{left:162px;top:2122px;font-size:29px;color:var(--ink)}
.news{top:2186px;width:274px;height:383px;background:#fff;border-top:4px solid var(--red);box-shadow:0 1px 4px rgba(0,0,0,.15)}
.news .date{position:absolute;left:11px;top:14px;width:52px;height:60px;background:var(--red-deep);clip-path:polygon(50% 0,100% 25%,100% 75%,50% 100%,0 75%,0 25%);color:#fff;text-align:center;font-family:"Rubik",sans-serif;line-height:1}
.date b{display:block;margin-top:15px;font-size:20px;font-weight:500}
.date span{font-size:12px}
.news h4{position:absolute;left:75px;top:28px;font-family:"Rubik",sans-serif;font-weight:500;font-size:16px;line-height:22px;color:var(--ink)}
.news .pic{position:absolute;left:0;top:95px;width:274px;height:159px}
.news p{position:absolute;left:24px;top:268px;width:236px;font-size:11.5px;line-height:16px;color:var(--muted)}
.news .more{position:absolute;left:24px;top:334px;font-family:"Rubik",sans-serif;font-weight:500;font-size:13px;color:var(--red)}
/* testimonial */
.testi{left:0;top:2642px;width:1200px;height:386px;background:linear-gradient(180deg,#9a1c36 0%,#8a1730 60%,#7a1229 100%)}
.testi-h{left:0;width:1200px;top:2725px;text-align:center;color:#fff;font-size:34px;font-weight:600}
.quote-mark{left:0;width:1200px;top:2770px;text-align:center;color:rgba(255,255,255,.45);font-family:Georgia,serif;font-size:80px;line-height:80px;font-weight:700}
.testi-p{left:0;width:1200px;top:2831px;text-align:center;color:#fff;font-size:18.5px;line-height:27px}
.testi-name{left:0;width:1158px;top:2929px;text-align:center;color:#fff;font-size:19px;font-weight:600;text-transform:uppercase}
/* footer */
.footer{left:0;top:3028px;width:1200px;height:397px;background:var(--footer)}
.footer-bottom{left:0;top:3349px;width:1200px;height:76px;background:var(--footer-bottom)}
.foot-brand{left:175px;top:3160px;font-family:"Rubik",sans-serif;font-weight:600;font-size:24px;color:#4a4a4a}
.fcol h5{font-family:"Rubik",sans-serif;font-weight:500;font-size:16px;color:#fff;text-transform:uppercase;margin-bottom:14px}
.fcol li{list-style:none;font-size:14px;color:#bbb;height:28px}
.fcol .row{display:flex;gap:12px;font-size:14px;color:#ccc;line-height:18px;margin-bottom:17px;align-items:flex-start}
.social-dot{width:14px;height:14px;background:#ddd;margin-top:2px;flex:none}
.copy{left:0;width:1200px;top:3376px;text-align:center;font-size:14px;color:#888}
</style>
</head>
<body>
<div class="abs top-line"></div>
<div class="abs call-tab">
  <svg width="18" height="18" viewBox="0 0 24 24"><path fill="#fff" d="M6.6 10.8a15 15 0 0 0 6.6 6.6l2.2-2.2c.3-.3.7-.4 1-.2 1.1.4 2.3.6 3.6.6.6 0 1 .4 1 1V20c0 .6-.4 1-1 1A17 17 0 0 1 3 4c0-.6.4-1 1-1h3.5c.6 0 1 .4 1 1 0 1.3.2 2.5.6 3.6.1.3 0 .7-.2 1z"/></svg>
  CALL US 01-555-0147
</div>
<div class="abs brand"><span class="brand-mark"></span>Brightwave Partners</div>
<nav class="nav">
  <a class="active" style="left:433px">HOME</a>
  <a style="left:513px">ABOUT US</a>
  <a style="left:629px">SERVICES</a>
  <a style="left:740px">STRATEGY</a>
  <a style="left:856px">IT NEWS</a>
  <a style="left:954px">CONTACT US</a>
</nav>

<div class="abs hero" role="img" aria-label="Two engineers working with a tablet between server racks in a data centre"></div>
<div class="abs circle-arrow" style="left:104px;top:359px"><svg width="18" height="18" viewBox="0 0 20 20"><path d="M13 3 6 10l7 7" fill="none" stroke="#222" stroke-width="2.4"/></svg></div>
<div class="abs circle-arrow" style="left:1040px;top:354px"><svg width="18" height="18" viewBox="0 0 20 20"><path d="M7 3l7 7-7 7" fill="none" stroke="#222" stroke-width="2.4"/></svg></div>
<div class="abs hero-title">WELCOME TO BRIGHTWAVE PARTNERS</div>
<div class="abs hero-sub">MISSION INTEGRITY RESULTS</div>
<div class="abs btn-solid">GET STARTED</div>

<div class="abs band"></div>
<svg class="abs" style="left:108px;top:820px" width="28" height="54" viewBox="0 0 28 54"><path d="M26 2 3 27l23 25" fill="none" stroke="#777" stroke-width="2"/></svg>
<svg class="abs" style="left:1072px;top:820px" width="28" height="54" viewBox="0 0 28 54"><path d="M2 2l23 25L2 52" fill="none" stroke="#777" stroke-width="2"/></svg>

<div class="abs svc" style="left:167px">
  <h3>Hardware /<br>Software Sales</h3>
  <div class="pic" role="img" aria-label="Glowing processor chip on a circuit board" style="background:radial-gradient(circle at 55% 55%,#cfe8ff 0%,#3c7bd0 18%,#14243f 55%,#0a0f1c 100%)"></div>
  <p>We have access to multiple distributor partners throughout North America, as well as Elite Partner Status</p>
  <div class="btn-line">Learn More</div>
</div>
<div class="abs svc" style="left:462px">
  <h3>Professional<br>Services</h3>
  <div class="pic" role="img" aria-label="Technician working in an aisle of server racks" style="background:linear-gradient(90deg,#1b1f26 0%,#3a4350 45%,#b7c0cb 55%,#2c333d 70%,#151a21 100%)"></div>
  <p>Our team provides experienced leadership and guidance, utilizing the industry standard methodologies.</p>
  <div class="btn-line">Learn More</div>
</div>
<div class="abs svc" style="left:757px">
  <h3>Technology<br>Assessment</h3>
  <div class="pic" role="img" aria-label="Hand touching a blue digital data interface" style="background:linear-gradient(135deg,#0b1e3a 0%,#1f5fa8 50%,#52b4ec 75%,#0d2a52 100%)"></div>
  <p>Experience has shown companies that perform objective, third-party technology assessments have proven</p>
  <div class="btn-line">Learn More</div>
</div>

<div class="abs about-pic" role="img" aria-label="Photo of server hardware and a technician at work"></div>
<div class="abs about-h head">Bringing thought leadership and<br>quality to every project</div>
<div class="abs about-p">Brightwave Partners, Inc. is an 8(a) full-service IT consulting company based in the Washington, DC Metro area. We offer specialized, highly customized technology solutions for our customers located throughout the United States</div>
<div class="abs btn-line" style="left:538px;top:1431px;width:165px;height:47px;font-size:15px">Learn More</div>

<div class="abs strategy"></div>
<div class="abs strategy-pic" role="img" aria-label="Two hands joining puzzle pieces over a network of connected points"></div>
<div class="abs strat-h head">Our Strategy</div>
<div class="abs strat-sub head">Your path to success</div>
<div class="abs strat-p">Civilian and Federal agencies are facing increased demands driven by the changing economic environment and shifts in the way products and services are sold and delivered.</div>
<div class="abs btn-line" style="left:166px;top:1920px;width:172px;height:48px;font-size:15px">Learn More</div>

<div class="abs news-h head">Latest News</div>
<div class="abs news" style="left:159px">
  <div class="date"><b>02</b><span>JAN</span></div>
  <h4>Pellentesque faucibus<br>Ut accumsan ultric</h4>
  <div class="pic" role="img" aria-label="Network of glowing connected nodes on a dark blue background" style="background:linear-gradient(135deg,#0c1630 0%,#23407a 55%,#0a1228 100%)"></div>
  <p>Duis quam Nam eget lacus Aliquam erat volutpat Quisque dignissim congue leo Mauris vel lacus vitae felis vestibulum</p>
  <div class="more">READ MORE</div>
</div>
<div class="abs news" style="left:464px">
  <div class="date"><b>10</b><span>JAN</span></div>
  <h4>Pellentesque faucibus<br>Ut accumsan ultric</h4>
  <div class="pic" role="img" aria-label="Engineer with a clipboard checking network cabling" style="background:linear-gradient(90deg,#7c8592 0%,#c9d1db 50%,#8e97a3 100%)"></div>
  <p>Duis quam Nam eget lacus Aliquam erat volutpat Quisque dignissim congue leo Mauris vel lacus vitae felis vestibulum</p>
  <div class="more">READ MORE</div>
</div>
<div class="abs news" style="left:770px">
  <div class="date"><b>20</b><span>JAN</span></div>
  <h4>Pellentesque faucibus<br>Ut accumsan ultric</h4>
  <div class="pic" role="img" aria-label="Technician inspecting a server rack in a data centre" style="background:linear-gradient(90deg,#2a3442 0%,#4f5e72 50%,#cfd6de 80%,#6d7888 100%)"></div>
  <p>Duis quam Nam eget lacus Aliquam erat volutpat Quisque dignissim congue leo Mauris vel lacus vitae felis vestibulum</p>
  <div class="more">READ MORE</div>
</div>

<div class="abs testi" role="img" aria-label="Faint server room backdrop tinted red"></div>
<div class="abs testi-h">Testimonials</div>
<div class="abs quote-mark">&ldquo;</div>
<svg class="abs" style="left:150px;top:2830px" width="48" height="30" viewBox="0 0 48 30"><path d="M46 15H3M16 2 3 15l13 13" fill="none" stroke="#fff" stroke-width="3"/></svg>
<svg class="abs" style="left:960px;top:2830px" width="48" height="30" viewBox="0 0 48 30"><path d="M2 15h43M32 2l13 13-13 13" fill="none" stroke="#fff" stroke-width="3"/></svg>
<div class="abs testi-p">Sed ut perspiciatis unde omnis iste natus error sit voluptatem<br>accusantium doloremque laudantium, totam rem aperiam, eaque ipsa<br>quae ab illo inventore veritatis et quasi architecto</div>
<div class="abs testi-name">Dana Whitfield</div>

<div class="abs footer"></div>
<div class="abs footer-bottom"></div>
<div class="abs foot-brand">Brightwave</div>
<div class="abs fcol" style="left:359px;top:3105px">
  <h5>Company</h5>
  <ul><li>Home</li><li>About us</li><li>Our Services</li><li>Why Us</li><li>Strategy</li></ul>
</div>
<div class="abs fcol" style="left:511px;top:3105px">
  <h5>Resources</h5>
  <ul style="margin-top:3px"><li>News</li><li>Testimonials</li><li>Term of Use</li><li>Sitemap</li><li>Contact Us</li></ul>
</div>
<div class="abs fcol" style="left:668px;top:3105px">
  <h5>Contact Us</h5>
  <div class="row"><svg width="16" height="18" viewBox="0 0 16 20"><path d="M8 1a6 6 0 0 0-6 6c0 5 6 12 6 12s6-7 6-12a6 6 0 0 0-6-6z" fill="none" stroke="#ccc" stroke-width="1.6"/><circle cx="8" cy="7" r="2" fill="none" stroke="#ccc" stroke-width="1.6"/></svg><span>4820 Larkspur Ct<br>Hollin Vale, MD 20999</span></div>
  <div class="row"><svg width="16" height="16" viewBox="0 0 24 24"><path d="M6.6 10.8a15 15 0 0 0 6.6 6.6l2.2-2.2c.3-.3.7-.4 1-.2 1.1.4 2.3.6 3.6.6.6 0 1 .4 1 1V20c0 .6-.4 1-1 1A17 17 0 0 1 3 4c0-.6.4-1 1-1h3.5c.6 0 1 .4 1 1 0 1.3.2 2.5.6 3.6.1.3 0 .7-.2 1z" fill="none" stroke="#ccc" stroke-width="1.6"/></svg><span>301-555-0147</span></div>
  <div class="row"><svg width="16" height="14" viewBox="0 0 20 16"><rect x="1" y="1" width="18" height="14" fill="none" stroke="#ccc" stroke-width="1.6"/><path d="M1 1l9 8 9-8" fill="none" stroke="#ccc" stroke-width="1.6"/></svg><span>info@brightwave.example</span></div>
</div>
<div class="abs fcol" style="left:901px;top:3105px">
  <h5>Social Media</h5>
  <div class="row"><span class="social-dot"></span><span>Friendsy</span></div>
  <div class="row"><span class="social-dot"></span><span>Chirpline</span></div>
  <div class="row"><span class="social-dot"></span><span>Workline</span></div>
  <div class="row"><span class="social-dot"></span><span>Snapfeed</span></div>
</div>
<div class="abs copy">&copy; 2019 Company Name&nbsp; All right reserved</div>
</body>
</html>
```